Resposive web site in 4 languages + image gallery + logo design

We need a web page, which will work on all devices.
I have uploaded web page concept.
Company name: Valqueno
Industry/Entity Type
It Company
Logo Text
quality matters
Coding
Coded - Design and coding required
Number of Pages Required
1 page

```html
<!DOCTYPE html>
<html lang="en">
<head>
<meta charset="utf-8">
<title>Valqueno — Woodworks, Stone Works &amp; Restoration</title>
<link href="https://fonts.googleapis.com/css2?family=Cinzel:wght@400;700&family=Lato:wght@400;700&display=swap" rel="stylesheet">
<style>
:root{
  --orange:#f7860f;
  --ink:#1d1d1d;
  --text:#3a3a3a;
  --white:#fff;
  --band:rgba(20,20,20,.72);
  --rule:#c9c9c9;
}
*{box-sizing:border-box;margin:0;padding:0}
html,body{width:681px;height:1200px;overflow:hidden;background:var(--white)}
body{position:relative;font-family:"Lato",sans-serif;color:var(--text)}
.abs{position:absolute}

/* top bar */
.topbar{left:0;top:0;width:681px;height:19px;background:var(--orange)}
.lang{top:3px;width:13px;height:13px;border-radius:50%;background:var(--white)}
.follow{left:533px;top:4px;font-size:8.5px;color:var(--white)}
.social{left:576px;top:3px;width:13px;height:13px;border-radius:50%;background:#3b5bb6}

/* header */
.brand{left:93px;top:38px;display:flex;align-items:center;gap:6px}
.brand-mark{width:12px;height:12px;background:var(--orange)}
.brand-name{font-family:"Cinzel",serif;font-weight:400;font-size:23px;color:var(--orange);letter-spacing:.5px;line-height:1}
.nav a{position:absolute;top:41px;font-size:8.5px;color:var(--ink);text-decoration:none;letter-spacing:.2px}
.nav .active{left:368px;top:35px;width:42px;height:21px;background:var(--orange);color:var(--white);border-radius:3px;text-align:center;line-height:21px}

/* hero */
.hero{left:0;top:71px;width:681px;height:298px;background:
  radial-gradient(ellipse 90px 120px at 96% 30%, rgba(236,228,210,.9) 0%, rgba(236,228,210,0) 100%),
  linear-gradient(180deg, rgba(44,66,56,.9) 0%, rgba(44,66,56,0) 24%),
  linear-gradient(180deg, rgba(0,0,0,0) 55%, rgba(125,118,106,.55) 78%, rgba(70,58,44,.55) 100%),
  radial-gradient(ellipse 150px 170px at 57% 78%, rgba(240,214,188,.75) 0%, rgba(240,214,188,0) 100%),
  linear-gradient(100deg,#7e3f15 0%,#a85a25 22%,#c27a44 40%,#d8a77c 55%,#b66a32 75%,#9a5a2c 90%,#d8c6a8 100%)}
.hero-arrow{top:188px}
.hero-band{left:0;top:337px;width:681px;height:32px;background:var(--band)}
.hero-ask{left:102px;top:343px;font-family:"Cinzel",serif;font-size:16px;color:var(--white);letter-spacing:.5px}
.hero-cta{left:446px;top:342px;width:115px;height:23px;border:1px solid #ffc27a;background:var(--orange);color:var(--white);font-family:"Cinzel",serif;font-size:15px;text-align:center;line-height:22px;border-radius:2px}

/* service tiles */
.tile{top:396px;width:161px;height:118px;overflow:hidden}
.tile-photo{width:100%;height:100%}
.tile-label{position:absolute;left:0;bottom:0;width:100%;height:20px;background:rgba(20,20,20,.75);color:var(--white);font-family:"Cinzel",serif;font-size:12px;line-height:21px;padding-left:9px}
.tile-plus{position:absolute;right:0;bottom:0;width:20px;height:20px;background:linear-gradient(135deg,transparent 50%,var(--orange) 50%)}
.tile-plus span{position:absolute;right:3px;bottom:0;color:var(--white);font-size:10px;font-weight:700}

/* section headings */
.section-title{left:0;width:681px;text-align:center;font-family:"Cinzel",serif;font-weight:400;font-size:17.5px;color:var(--ink);letter-spacing:.8px}
.section-title em{font-style:normal;color:var(--orange)}
.section-rule{left:262px;width:157px;border-top:1px dotted var(--rule)}
.about-lead{left:0;top:582px;width:681px;text-align:center;font-size:7.4px;font-weight:700;color:var(--ink)}
.about-text{left:96px;top:595px;width:489px;text-align:center;font-size:7.4px;line-height:11.5px;color:var(--text)}
.btn-more{left:313px;top:626px;width:55px;height:16px;background:var(--orange);color:var(--white);font-size:7.5px;font-weight:700;text-align:center;line-height:16px;border-radius:2px}

/* gallery */
.photo{position:absolute}
.gallery-caption{left:111px;top:771px;width:140px;text-align:center;color:var(--white)}
.gallery-caption h3{font-family:"Cinzel",serif;font-weight:400;font-size:11px;margin-bottom:7px}
.gallery-caption p{font-size:6.6px;line-height:9.5px}
.gallery-arrow{top:846px}

/* footer */
.footer{left:0;top:998px;width:681px;height:180px;background:
  radial-gradient(ellipse 120px 60px at 30% 35%, rgba(140,96,52,.35) 0%, rgba(140,96,52,0) 100%),
  radial-gradient(ellipse 140px 70px at 72% 60%, rgba(120,84,46,.3) 0%, rgba(120,84,46,0) 100%),
  linear-gradient(180deg,#2a2521 0%,#221d19 60%,#1a1613 100%)}
.foot-title{font-family:"Cinzel",serif;font-size:9.5px;color:var(--white);letter-spacing:.4px;display:flex;align-items:center;gap:6px}
.field{position:absolute;border:1px solid #cfcfcf;height:21px;color:#ddd;font-size:7px;padding:6px 5px}
.submit{left:273px;top:1141px;width:52px;height:19px;background:var(--orange);color:var(--ink);font-family:"Cinzel",serif;font-weight:700;font-size:10px;text-align:center;line-height:19px}
.links{left:366px;top:1053px;list-style:none}
.links li{font-size:7px;color:#e6e6e6;height:13px}
.links li::before{content:"›";color:#bbb;margin-right:6px}
.links li.current{color:var(--orange);font-weight:700}
.contact{left:486px;font-size:7px;color:#e6e6e6;line-height:11px}
.copyright{left:0;top:1178px;width:681px;height:22px;background:var(--orange);color:var(--white);font-size:6.5px;text-align:center;line-height:22px}
</style>
</head>
<body>

<div class="abs topbar"></div>
<span class="abs lang" style="left:453px"></span>
<span class="abs lang" style="left:470px"></span>
<span class="abs lang" style="left:487px"></span>
<span class="abs lang" style="left:504px"></span>
<span class="abs follow">Follow Us</span>
<span class="abs social"></span>

<div class="abs brand"><span class="brand-mark"></span><span class="brand-name">VALQUENO</span></div>
<nav class="nav">
  <a class="active" href="#">HOME</a>
  <a href="#" style="left:423px">ABOUT US</a>
  <a href="#" style="left:484px">SERVICES</a>
  <a href="#" style="left:534px">CONTACT US</a>
</nav>

<div class="abs hero" role="img" aria-label="Photo of a smiling family in front of a log house with a stone base"></div>
<svg class="abs hero-arrow" style="left:44px" width="16" height="30" viewBox="0 0 16 30"><polyline points="14,2 2,15 14,28" fill="none" stroke="#fff" stroke-width="1.5"/></svg>
<svg class="abs hero-arrow" style="left:624px" width="16" height="30" viewBox="0 0 16 30"><polyline points="2,2 14,15 2,28" fill="none" stroke="#fff" stroke-width="1.5"/></svg>
<div class="abs hero-band"></div>
<div class="abs hero-ask">ARE YOU INTERESTED IN AN ESTIMATE?</div>
<div class="abs hero-cta">Get a Quote</div>

<div class="abs tile" style="left:92px">
  <div class="tile-photo" role="img" aria-label="Photo of a two-storey wooden house" style="background:
    linear-gradient(180deg,rgba(200,215,225,.8) 0%,rgba(200,215,225,0) 22%),
    radial-gradient(ellipse 40px 70px at 8% 45%,rgba(70,110,50,.9) 0%,rgba(70,110,50,0) 100%),
    linear-gradient(180deg,#a86a3a 10%,#d89a48 40%,#c97f30 70%,#6a7a40 100%)"></div>
  <div class="tile-label">WOODWORKS</div><div class="tile-plus"><span>+</span></div>
</div>
<div class="abs tile" style="left:260px">
  <div class="tile-photo" role="img" aria-label="Photo of a stone cottage" style="background:
    linear-gradient(180deg,rgba(225,230,235,.9) 0%,rgba(225,230,235,0) 20%),
    radial-gradient(ellipse 60px 40px at 80% 12%,rgba(80,110,60,.8) 0%,rgba(80,110,60,0) 100%),
    linear-gradient(180deg,#6a6258 15%,#8a6e58 45%,#6f5a48 70%,#3e3a34 100%)"></div>
  <div class="tile-label">STONE WORKS</div><div class="tile-plus"><span>+</span></div>
</div>
<div class="abs tile" style="left:428px">
  <div class="tile-photo" role="img" aria-label="Photo of a stone building under restoration with scaffolding" style="background:
    linear-gradient(180deg,rgba(232,236,240,.95) 0%,rgba(232,236,240,0) 22%),
    radial-gradient(ellipse 50px 40px at 88% 85%,rgba(70,110,55,.9) 0%,rgba(70,110,55,0) 100%),
    linear-gradient(180deg,#8f8a84 20%,#7d7770 55%,#9a9690 80%,#5c6650 100%)"></div>
  <div class="tile-label">RESTORATION</div><div class="tile-plus"><span>+</span></div>
</div>

<h2 class="abs section-title" style="top:548px">ABOUT <em>VALQUENO</em></h2>
<div class="abs section-rule" style="top:574px"></div>
<p class="abs about-lead">Valqueno Is A Company Whose Business Operations Include Making Wooden Products, Restoration And Building Structures From Natural Stone.</p>
<p class="abs about-text">All of our products are made by craftsmen and specialists who have extensive experience and knowledge in their fields. The products we offer are always handmade and we take the requests and ideas of the specific client into account We always strive to achieve the best possible quality.</p>
<div class="abs btn-more">READ MORE</div>

<h2 class="abs section-title" style="top:680px">PROJECT <em>GALLERY</em></h2>
<div class="abs section-rule" style="top:704px"></div>

<div class="photo" role="img" aria-label="Photo of a timber frame porch at dusk" style="left:92px;top:716px;width:178px;height:153px;background:
  radial-gradient(ellipse 90px 50px at 40% 20%,rgba(140,80,40,.6) 0%,rgba(140,80,40,0) 100%),
  linear-gradient(180deg,#3e2616 0%,#2a1a10 60%,#1a110a 100%)"></div>
<div class="abs gallery-caption">
  <h3>LOREM IPSUM</h3>
  <p>Lorem ipsum dolor sit amet, consectetuer adipiscing elit, sed diam nonummy nibh eu</p>
</div>
<div class="photo" role="img" aria-label="Photo of a white house above a stone retaining wall" style="left:275px;top:716px;width:187px;height:72px;background:
  linear-gradient(180deg,#5f7a48 0%,#d8dcd8 30%,#a9a59c 55%,#8a857a 75%,#5c8c34 100%)"></div>
<div class="photo" role="img" aria-label="Photo of a brick house" style="left:275px;top:792px;width:92px;height:77px;background:
  linear-gradient(180deg,#c8cdd2 0%,#8a8680 25%,#a8613e 50%,#8e4e30 80%,#5a4a38 100%)"></div>
<div class="photo" role="img" aria-label="Photo of a grey stone house" style="left:372px;top:792px;width:90px;height:77px;background:
  linear-gradient(180deg,#dfe3e6 0%,#8c8e90 30%,#b3b0a8 55%,#9a968c 80%,#6a7058 100%)"></div>
<div class="photo" role="img" aria-label="Photo of a stone house with white windows" style="left:467px;top:716px;width:122px;height:153px;background:
  linear-gradient(180deg,#b6b9bb 0%,#6e6b68 28%,#7a7570 55%,#5e6a4a 80%,#4a6a30 100%)"></div>
<div class="photo" role="img" aria-label="Photo of a wooden house with a red roof" style="left:92px;top:874px;width:275px;height:102px;background:
  linear-gradient(180deg,#d6dadd 0%,#8a7258 30%,#a86e42 50%,#8a2c2c 72%,#6a4a34 100%)"></div>
<div class="photo" role="img" aria-label="Photo of a wooden staircase interior" style="left:370px;top:874px;width:219px;height:102px;background:
  radial-gradient(ellipse 60px 60px at 30% 60%,rgba(230,140,60,.7) 0%,rgba(230,140,60,0) 100%),
  linear-gradient(100deg,#6e2e0c,#b85e1e 35%,#8a3e12 60%,#c2702c 80%,#6b2e0e)"></div>
<svg class="abs gallery-arrow" style="left:60px" width="16" height="30" viewBox="0 0 16 30"><polyline points="14,2 2,15 14,28" fill="none" stroke="#555" stroke-width="1"/></svg>
<svg class="abs gallery-arrow" style="left:604px" width="16" height="30" viewBox="0 0 16 30"><polyline points="2,2 14,15 2,28" fill="none" stroke="#555" stroke-width="1"/></svg>

<footer>
<div class="abs footer" role="img" aria-label="Darkened photo of a stone house at night"></div>

<div class="abs foot-title" style="left:99px;top:1030px">
  <svg width="12" height="12" viewBox="0 0 12 12"><rect x="1" y="2" width="10" height="9" fill="none" stroke="#f7860f" stroke-width="1.2"/><line x1="1" y1="5" x2="11" y2="5" stroke="#f7860f"/><line x1="4" y1="0.5" x2="4" y2="3" stroke="#f7860f"/><line x1="8" y1="0.5" x2="8" y2="3" stroke="#f7860f"/></svg>
  QUICK INQUIRY
</div>
<div class="field" style="left:98px;top:1053px;width:227px">Name</div>
<div class="field" style="left:98px;top:1082px;width:108px">Phone</div>
<div class="field" style="left:218px;top:1082px;width:107px">Email</div>
<div class="field" style="left:98px;top:1112px;width:227px">Message</div>
<div class="abs submit">SUBMIT</div>

<div class="abs foot-title" style="left:352px;top:1030px">
  <svg width="10" height="12" viewBox="0 0 10 12"><rect x="1" y="1" width="8" height="10" fill="none" stroke="#f7860f" stroke-width="1.2"/><line x1="3" y1="4" x2="7" y2="4" stroke="#f7860f"/><line x1="3" y1="6.5" x2="7" y2="6.5" stroke="#f7860f"/></svg>
  QUICK LINKS
</div>
<ul class="abs links">
  <li class="current">Home</li>
  <li>About Us</li>
  <li>Services</li>
  <li>Contact Us</li>
</ul>

<div class="abs foot-title" style="left:474px;top:1030px">
  <svg width="12" height="12" viewBox="0 0 12 12"><circle cx="6" cy="6" r="5" fill="none" stroke="#f7860f" stroke-width="1.2"/><ellipse cx="6" cy="6" rx="2.2" ry="5" fill="none" stroke="#f7860f"/><line x1="1" y1="6" x2="11" y2="6" stroke="#f7860f"/></svg>
  CONTACT DETAILS
</div>
<svg class="abs" style="left:474px;top:1055px" width="8" height="11" viewBox="0 0 8 11"><path d="M4 0.5a3.5 3.5 0 0 1 3.5 3.5c0 2.6-3.5 6.5-3.5 6.5S0.5 6.6 0.5 4A3.5 3.5 0 0 1 4 0.5z" fill="#f7860f"/><circle cx="4" cy="4" r="1.3" fill="#1f1b18"/></svg>
<div class="abs contact" style="top:1055px">Harbour Lane 12<br>10415 Norvik<br>ELDMARK</div>
<svg class="abs" style="left:474px;top:1092px" width="9" height="9" viewBox="0 0 9 9"><path d="M1.5 0.5l2 2-1 1.2a5 5 0 0 0 2.8 2.8l1.2-1 2 2-1.3 1.3C4 8.5 0.5 5 0.2 1.8z" fill="#f7860f"/></svg>
<div class="abs contact" style="top:1092px;font-weight:700">+321 54 09876</div>
<svg class="abs" style="left:474px;top:1110px" width="9" height="7" viewBox="0 0 9 7"><rect x="0" y="0" width="9" height="7" fill="#f7860f"/><polyline points="0,0 4.5,3.8 9,0" fill="none" stroke="#1f1b18" stroke-width=".8"/></svg>
<div class="abs contact" style="top:1109px">sales@valqueno.com</div>

<div class="abs copyright">Copyright © 2016 Valqueno. All Right Reserved.</div>
</footer>

</body>
</html>
```